IT Company needs a Wordpress Web Design

We need a wordpress website for a new IT Company called 'RQ Systems'. We develop educational software for Middle and High School Students and Staff. Our initial product is BrightDesk - a web app that allows School Counselors to track information about the students that they see. We would like to see modern designs that include the company logo and the BrightDesk logo

Target Market(s)

Educators

Industry/Entity Type

Information Technology

Coding

Coded - Design and coding required

Number of Pages Required

1 page

Font styles to use
Sans Serif

Requirements
Must have
• Must be able to use WordPress
Should not have
• No Flash

```html
<!DOCTYPE html>
<html lang="en">
<head>
<meta charset="utf-8">
<title>RQ Systems</title>
<link rel="stylesheet" href="https://fonts.googleapis.com/css2?family=Open+Sans:wght@400;600;700&family=Oswald:wght@400&display=swap">
<style>
:root{
  --blue:#4784c4;
  --blue-dark:#3a73b0;
  --text:#333;
  --muted:#555;
  --line:#d6d6d6;
  --soft:#f2f2f2;
  --white:#fff;
}
*{box-sizing:border-box;margin:0;padding:0}
html,body{width:1200px;height:2927px;overflow:hidden}
body{font-family:"Open Sans",Arial,sans-serif;color:var(--text);background:var(--white)}
.wrap{width:936px;margin:0 auto;position:relative}
section,header,footer{position:relative;width:1200px}

/* hero */
.hero{height:615px;overflow:hidden}
.hero-photo{position:absolute;inset:0;background:linear-gradient(120deg,#d9dcdf 0%,#9aa3ab 30%,#5e6670 55%,#c4c8cc 80%,#eceeef 100%)}
.nav{position:absolute;left:445px;top:0;width:624px;height:39px;background:var(--blue);display:flex;align-items:center;justify-content:space-around;padding:0 14px}
.nav a{color:var(--white);text-decoration:none;font-size:11.5px;font-weight:600;letter-spacing:.2px}
.nav a.active{text-decoration:underline}
.brand{position:absolute;left:131px;top:0;width:156px;height:113px;background:var(--white);display:flex;align-items:center;justify-content:center;gap:8px}
.brand-mark{width:14px;height:14px;background:var(--blue)}
.brand-name{color:var(--blue);font-weight:700;font-size:18px}
.slide-arrow{position:absolute;top:290px;width:24px;height:32px;background:rgba(120,120,120,.7);display:flex;align-items:center;justify-content:center}
.slide-arrow.left{left:0}.slide-arrow.right{right:0}

/* intro */
.intro{height:341px;text-align:center}
.intro h1{padding-top:72px;color:var(--blue);font-weight:600;font-size:25px;line-height:34px}
.intro p{margin:16px auto 0;width:936px;font-size:11.5px;line-height:21px;color:var(--muted)}
.btn{display:inline-block;margin-top:17px;width:96px;height:35px;line-height:33px;border:1px solid #bbb;font-size:11px;color:#555;text-decoration:none}

/* product */
.product{height:402px;color:var(--white);text-align:center;overflow:hidden}
.product-photo{position:absolute;inset:0;background:linear-gradient(110deg,#5b8fc6 0%,#4a83c0 45%,#3f79b8 75%,#5a8dc4 100%)}
.product .wrap{padding-top:92px}
.product h2{font-size:31px;font-weight:700;letter-spacing:.5px}
.product h3{margin-top:10px;font-size:15.5px;font-weight:600}
.product p{margin-top:4px;font-size:11.5px;line-height:21px}
.product-brand{margin-top:34px;display:inline-flex;align-items:center;gap:10px;font-weight:700;font-size:22px}
.product-brand span.sq{width:18px;height:18px;background:var(--white)}

/* projects */
.projects{height:507px}
.projects .wrap{padding-top:74px}
.section-title{color:var(--blue);font-size:24px;font-weight:400}
.carousel-ctrl{position:absolute;right:0;top:82px;display:flex;gap:6px}
.carousel-ctrl span{width:20px;height:20px;border-radius:50%;border:1px solid #bbb;display:flex;align-items:center;justify-content:center}
.cards{margin-top:20px;display:flex;justify-content:space-between}
.card{width:289px}
.card-photo{height:191px}
.card h4{margin-top:14px;font-size:17px;font-weight:400;line-height:23px;color:#222}
.card p{margin-top:10px;font-size:10.5px;line-height:17px;color:var(--muted)}

/* pricing */
.pricing{height:480px;background:var(--soft)}
.pricing .section-title{text-align:center;padding-top:70px}
.plans{margin-top:20px;display:flex;justify-content:center;gap:28px}
.plan{width:361px;height:279px;background:var(--white);box-shadow:0 1px 5px rgba(0,0,0,.12)}
.plan-head{height:106px;padding:24px 26px 0;border-bottom:1px solid var(--line)}
.plan-head h5{color:var(--blue);font-size:16px;font-weight:400}
.price{margin-top:6px;font-family:"Oswald",Arial,sans-serif;font-size:26px}
.price small{font-family:"Open Sans",Arial,sans-serif;font-size:9.5px;margin-left:6px}
.plan ul{list-style:none;padding:24px 20px 0 26px}
.plan li{font-size:10px;line-height:25.5px;display:flex;align-items:center;gap:10px;white-space:nowrap}
.plan li em{font-style:normal;color:var(--blue)}

/* faq */
.faq{height:398px}
.faq .section-title{text-align:center;padding-top:76px}
.tabs{margin-top:18px;display:flex;justify-content:space-between}
.tab{width:218px;height:47px;border:1px solid #c9c9c9;color:var(--blue);font-size:16px;display:flex;align-items:center;justify-content:center;position:relative}
.tab.active{background:var(--blue);color:var(--white);border-color:var(--blue)}
.tab.active::after{content:"";position:absolute;bottom:-9px;left:50%;margin-left:-9px;border-left:9px solid transparent;border-right:9px solid transparent;border-top:9px solid var(--blue)}
.faq h6{margin-top:36px;text-align:center;font-size:20px;font-weight:600;color:#222}
.faq p{margin-top:12px;font-size:10.5px;line-height:21px;color:var(--muted)}

/* footer */
.site-footer{height:184px;background:#f4f4f4}
.social{padding-top:43px;display:flex;justify-content:center;gap:30px}
.social span{width:12px;height:12px;border-radius:50%;background:#444}
.footer-line{margin-top:36px;border-top:1px solid var(--line)}
.footer-bar{margin-top:32px;display:flex;justify-content:space-between;font-size:11px;color:#444}
.footer-bar nav a{color:#444;text-decoration:none}
.footer-bar nav i{font-style:normal;margin:0 9px}
</style>
</head>
<body>

<header class="hero">
  <div class="hero-photo" role="img" aria-label="Photo of people working together at desktop computers in a bright office"></div>
  <div class="brand"><span class="brand-mark"></span><span class="brand-name">RQ Systems</span></div>
  <nav class="nav">
    <a class="active" href="#">HOME</a><a href="#">ABOUT US</a><a href="#">SERVICES</a><a href="#">PROJECTS</a><a href="#">CONTACT US</a><a href="#">LOGIN</a>
    <svg width="12" height="12" viewBox="0 0 12 12" aria-label="Search"><circle cx="5" cy="5" r="3.6" fill="none" stroke="#fff" stroke-width="1.8"/><line x1="7.6" y1="7.6" x2="11" y2="11" stroke="#fff" stroke-width="2"/></svg>
  </nav>
  <span class="slide-arrow left"><svg width="8" height="12" viewBox="0 0 8 12"><path d="M6 1 1 6l5 5" fill="none" stroke="#fff" stroke-width="1.6"/></svg></span>
  <span class="slide-arrow right"><svg width="8" height="12" viewBox="0 0 8 12"><path d="M2 1l5 5-5 5" fill="none" stroke="#fff" stroke-width="1.6"/></svg></span>
</header>

<section class="intro">
  <h1>We develop educational software for<br>Middle and High School Students and Staff.</h1>
  <p>Phasellus nec erat dictum, vehicula lacus sed, efficitur nunc. Sed vel scelerisque nibh. Curabitur id mattis massa. Nullam vel dui eget eros pellentesque rhoncus eget at sapien. Quisque vestibulum justo ipsum, sit amet faucibus odio imperdiet ut. Maecenas viverra et nunc ac sollicitudin. Integer egestas semper dolor, et tincidunt diam rutrum non. Etiam sodales purus id ultricies pellentesque. Etiam vel augue efficitur elit interdum placerat. Curabitur eget magna metus.</p>
  <a class="btn" href="#">READ MORE</a>
</section>

<section class="product">
  <div class="product-photo" role="img" aria-label="Blue-tinted photo of a classroom computer lab"></div>
  <div class="wrap">
    <h2>OUR PRODUCT</h2>
    <h3>A web app that allows School Counselors to track information about the students that they see</h3>
    <p>Phasellus nec erat dictum, vehicula lacus sed, efficitur nunc. Sed vel scelerisque nibh. Curabitur id mattis massa. Nullam vel dui eget eros pellentesque rhoncus eget at sapien. Quisque vestibulum justo ipsum, sit amet faucibus odio imperdiet ut. Maecenas viverra et nunc ac sollicitudin. Integer egestas semper dolor, et tincidunt diam rutrum non. Etiam sodales purus id ultricies pellentesque. Etiam vel augue efficitur elit interdum placerat. Curabitur eget magna metus.</p>
    <div class="product-brand"><span class="sq"></span>BrightDesk</div>
  </div>
</section>

<section class="projects">
  <div class="wrap">
    <h2 class="section-title">Our Projects</h2>
    <div class="carousel-ctrl">
      <span><svg width="6" height="8" viewBox="0 0 6 8"><path d="M5 0v8L0 4z" fill="#333"/></svg></span>
      <span><svg width="6" height="8" viewBox="0 0 6 8"><path d="M1 0v8l5-4z" fill="#333"/></svg></span>
    </div>
    <div class="cards">
      <article class="card">
        <div class="card-photo" role="img" aria-label="Laptop showing code on a desk" style="background:linear-gradient(135deg,#2c3138,#6b7077 60%,#c9c4bc)"></div>
        <h4>Integer at massa vitae erat egestas vo lutpat et sit amet diam</h4>
        <p>Morbi eget justo consequat magna venenatis lacinia. Maecenas eu viverra tellus. Nulla et suscipit leo, id tincidunt nulla. In aliquet et augue eu convallis.</p>
      </article>
      <article class="card">
        <div class="card-photo" role="img" aria-label="Student writing notes beside a laptop" style="background:linear-gradient(135deg,#b58a5e,#e4d4c0 55%,#f4efe8)"></div>
        <h4>Integer at massa vitae erat egestas vo lutpat et sit amet diam</h4>
        <p>Morbi eget justo consequat magna venenatis lacinia. Maecenas eu viverra tellus. Nulla et suscipit leo, id tincidunt nulla. In aliquet et augue eu convallis.</p>
      </article>
      <article class="card">
        <div class="card-photo" role="img" aria-label="Students working with lab equipment and a laptop" style="background:linear-gradient(135deg,#8c949c,#d3d6d8 50%,#a8b2ba)"></div>
        <h4>Integer at massa vitae erat egestas vo lutpat et sit amet diam</h4>
        <p>Morbi eget justo consequat magna venenatis lacinia. Maecenas eu viverra tellus. Nulla et suscipit leo, id tincidunt nulla. In aliquet et augue eu convallis.</p>
      </article>
    </div>
  </div>
</section>

<section class="pricing">
  <h2 class="section-title">Pricing</h2>
  <div class="plans">
    <div class="plan">
      <div class="plan-head"><h5>Individual School Purchase</h5><div class="price">$200<small>per school</small></div></div>
      <ul>
        <li><svg width="9" height="8" viewBox="0 0 9 8"><path d="M1 4l2.5 2.5L8 1" fill="none" stroke="#333" stroke-width="1.6"/></svg><span><em>12 months</em> of access to BrightDesk</span></li>
        <li><svg width="9" height="8" viewBox="0 0 9 8"><path d="M1 4l2.5 2.5L8 1" fill="none" stroke="#333" stroke-width="1.6"/></svg><span><em>Individual Accounts</em> for each school counselor in your office</span></li>
        <li><svg width="9" height="8" viewBox="0 0 9 8"><path d="M1 4l2.5 2.5L8 1" fill="none" stroke="#333" stroke-width="1.6"/></svg><span><em>Customizable</em> Student Login Screen</span></li>
        <li><svg width="9" height="8" viewBox="0 0 9 8"><path d="M1 4l2.5 2.5L8 1" fill="none" stroke="#333" stroke-width="1.6"/></svg><span>Access to a variety of <em>Data Reports</em> in Sheetly and PDF format</span></li>
        <li><svg width="9" height="8" viewBox="0 0 9 8"><path d="M1 4l2.5 2.5L8 1" fill="none" stroke="#333" stroke-width="1.6"/></svg><span>Email <em>Product Support</em></span></li>
      </ul>
    </div>
    <div class="plan">
      <div class="plan-head"><h5>District Level Purchase</h5><div class="price">$150<small>per school</small></div></div>
      <ul>
        <li><svg width="9" height="8" viewBox="0 0 9 8"><path d="M1 4l2.5 2.5L8 1" fill="none" stroke="#333" stroke-width="1.6"/></svg><span><em>12 months</em> of access to BrightDesk</span></li>
        <li><svg width="9" height="8" viewBox="0 0 9 8"><path d="M1 4l2.5 2.5L8 1" fill="none" stroke="#333" stroke-width="1.6"/></svg><span><em>Individual Accounts</em> for each school counselor in your office</span></li>
        <li><svg width="9" height="8" viewBox="0 0 9 8"><path d="M1 4l2.5 2.5L8 1" fill="none" stroke="#333" stroke-width="1.6"/></svg><span><em>Customizable</em> Student Login Screen</span></li>
        <li><svg width="9" height="8" viewBox="0 0 9 8"><path d="M1 4l2.5 2.5L8 1" fill="none" stroke="#333" stroke-width="1.6"/></svg><span>Access to a variety of <em>Data Reports</em> in Sheetly and PDF format</span></li>
        <li><svg width="9" height="8" viewBox="0 0 9 8"><path d="M1 4l2.5 2.5L8 1" fill="none" stroke="#333" stroke-width="1.6"/></svg><span>Email <em>Product Support</em></span></li>
      </ul>
    </div>
  </div>
</section>

<section class="faq">
  <div class="wrap">
    <h2 class="section-title">FAQs</h2>
    <div class="tabs">
      <div class="tab">WHAT?</div><div class="tab active">WHY?</div><div class="tab">HOW?</div><div class="tab">WHO?</div>
    </div>
    <h6>Why should i buy BrightDesk?</h6>
    <p>Mauris blandit condimentum urna, ac porttitor urna vestibulum nec. Curabitur ac sollicitudin enim. Sed lectus velit, accumsan in purus a, interdum sodales mi. Sed ut posuere quam, a sagittis lacus. Nulla viverra, odio a luctus pharetra, felis purus ornare nisl, quis ultricies libero augue luctus lacus. Integer cursus lacus vel nisi facilisis, quis sagittis dui consectetur. Nunc mollis cursus ante. Aliquam sodales, orci at tempor consequat, quam purus viverra nisl, sed accumsan nulla lectus eget nulla. Nam et erat ligula. Proin tortor nibh, vestibulum sit amet nunc at, blandit suscipit libero. Ut nec est id tortor egestas convallis a et nibh.</p>
  </div>
</section>

<footer class="site-footer">
  <div class="social" aria-label="Social links"><span></span><span></span><span></span><span></span></div>
  <div class="wrap">
    <div class="footer-line"></div>
    <div class="footer-bar">
      <nav><a href="#">Home</a><i>|</i><a href="#">About Us</a><i>|</i><a href="#">Services</a><i>|</i><a href="#">Projects</a><i>|</i><a href="#">Contact Us</a><i>|</i><a href="#">vLogin</a></nav>
      <span>Copyright &copy; 2017 &nbsp;Company name. &nbsp;All rights reserved.</span>
    </div>
  </div>
</footer>

</body>
</html>
```